BriskLoom Wordpress Website

We require a WordPress website that emulates the sleek design and functionality of https://www.tulvorix.example and https://quenlap.example/. The site should showcase our AI-powered customer support solutions with a modern, professional aesthetic.
Homepage
The homepage should feature a bold headline highlighting our AI capabilities, followed by concise sections outlining our key offerings:
AI-powered customer support
Data integration and deployment
Knowledge system integration
AI help desks and chat agents
Customer feedback insights
Include eye-catching visuals or animations to illustrate these concepts.
Navigation
The main navigation menu should include:
Product
Platform
Company
News
Learn More
Key Pages
Product Page: Detail our AI solutions, their benefits, and use cases.
Platform Page: Explain our technology, integration capabilities, and deployment process.
Company Page: Share our mission, team, and values.
News Page: Feature latest updates, press releases, and blog posts.
Call-to-Action
Implement a prominent "Learn More" button that directs users to an enrollment page. Our team will manage inquiries from this point.
Footer
Include a "Contact Us" section in the footer for easy access to our contact information.
Design Elements
Use a clean, minimalist design with ample white space
Incorporate a color scheme that reflects trust and innovation
Utilize smooth scrolling and subtle animations for enhanced user experience
Ensure mobile responsiveness for all devices
Technical Requirements
Build on WordPress for easy content management
Optimize for fast loading speeds and SEO
The website should convey our expertise in AI-driven customer support solutions while providing an intuitive user experience that guides visitors toward learning more about our services
Industry/Entity Type
AI Chat Agents

```html
<!DOCTYPE html>
<html lang="en">
<head>
<meta charset="utf-8">
<title>BriskLoom – AI Customer Support</title>
<link href="https://fonts.googleapis.com/css2?family=Lato:wght@400;700;900&display=swap" rel="stylesheet">
<style>
:root{
  --teal-dark:#2a5a5d;
  --teal:#3a7c80;
  --teal-light:#4e9599;
  --ink:#1d1d1d;
  --muted:#555;
  --footer:#2e2f30;
  --white:#fff;
}
*{box-sizing:border-box;margin:0;padding:0}
html,body{width:1200px;height:2913px;overflow:hidden}
body{position:relative;font-family:'Lato',sans-serif;color:var(--ink);background:var(--white)}
.abs{position:absolute}
a{color:inherit;text-decoration:none}

.hero{position:absolute;left:0;top:0;width:1200px;height:612px;overflow:hidden}
.hero-wave{position:absolute;left:0;top:0}
.brand{position:absolute;display:flex;align-items:center;gap:10px;font-weight:400;white-space:nowrap}
.brand-dot{width:56px;height:56px;border-radius:50%;background:var(--teal-dark)}
.brand-name{font-size:40px;color:var(--teal-dark)}
.nav{position:absolute;left:441px;top:42px;display:flex;gap:33px;font-size:15px;color:var(--ink)}
.nav .active{color:var(--teal-dark);font-weight:700}
.btn{display:inline-flex;align-items:center;justify-content:center;border-radius:22px;font-weight:700;font-size:15px}
.btn-teal{background:var(--teal-dark);color:var(--white)}
.btn-white{background:var(--white);color:var(--ink)}
.hero-kicker{left:111px;top:184px;font-size:22px}
.hero-title{left:109px;top:222px;font-size:52px;font-weight:900;letter-spacing:-.5px;white-space:nowrap}
.hero-title span{color:var(--teal-dark)}
.hero-art{left:582px;top:188px;width:618px;height:428px;border-radius:14px 0 0 0;background:linear-gradient(135deg,#3d7f83 0%,#9cc7c8 60%,#dfe9ea 100%)}
.dots{left:576px;top:534px;display:flex;gap:4px}
.dots i{width:8px;height:8px;border-radius:50%;background:#fff;display:block}

.card{position:absolute;top:695px;width:269px;height:275px;border-radius:14px;background:#fff;box-shadow:0 2px 14px rgba(0,0,0,.07);padding:18px 30px}
.card.is-active{border:2px solid var(--teal-dark);box-shadow:none}
.card .icon{height:82px;display:flex;align-items:center}
.card p{margin-top:20px;font-size:16px;line-height:33px;color:var(--muted)}

.interactions{position:absolute;left:0;top:1060px;width:1200px;height:597px;background:var(--teal-dark);color:#fff;overflow:hidden}
.interactions h2{position:absolute;left:111px;top:80px;font-size:44px;font-weight:400;line-height:51px}
.interactions h2 b{font-weight:900}
.interactions .lead{position:absolute;left:111px;top:198px;font-size:22px;font-weight:700}
.benefit{position:absolute;left:111px;display:flex;gap:27px}
.benefit .ic{width:72px;height:72px;border-radius:50%;background:#f2f4f4;display:flex;align-items:center;justify-content:center;flex:none}
.benefit h3{font-size:22px;font-weight:400;margin-top:4px}
.benefit p{font-size:13.5px;margin:8px 0 0 4px;line-height:22px;max-width:320px}
.int-art{left:643px;top:82px;width:460px;height:460px;border-radius:50%;background:radial-gradient(circle at 50% 45%,#ffffff,#dbe9f3 60%,#c4dceb)}

.tabs{position:absolute;top:1737px;left:0;width:1200px;font-size:17px}
.tabs div{position:absolute;line-height:22px;white-space:nowrap}
.tabs .current{color:var(--teal-dark);font-weight:700;text-decoration:underline}

.trust{position:absolute;left:111px;top:1832px;width:967px;height:323px;border-radius:14px;background:#fff;box-shadow:0 2px 14px rgba(0,0,0,.1)}
.trust-art{left:50px;top:22px;width:235px;height:274px;border-radius:12px;background:linear-gradient(160deg,#cfe4e2,#eef3f3 70%)}
.trust h2{position:absolute;left:350px;top:44px;font-size:34px;font-weight:400;white-space:nowrap}
.trust h2 b{color:var(--teal-dark);font-weight:700}
.pillar{position:absolute;top:130px;font-size:17px;line-height:22px}
.pillar svg{display:block;margin-bottom:18px}

.footer-bg{position:absolute;left:0;top:2410px;width:1200px;height:503px;background:var(--footer)}
.cta{position:absolute;left:111px;top:2245px;width:977px;height:292px;border-radius:146px;background:linear-gradient(180deg,var(--teal-light),var(--teal-dark));color:#fff;text-align:center}
.cta h2{margin-top:44px;font-size:35px;font-weight:900;line-height:48px;white-space:nowrap}
.cta .btn{margin-top:16px;width:131px;height:38px;font-size:14px;border-radius:19px}

.footer{position:absolute;left:0;top:2560px;width:1200px;color:#fff}
.footer .brand-dot{background:#fff;width:62px;height:62px}
.footer .brand-name{color:#fff;font-size:42px}
.stay{left:434px;top:46px}
.stay h3{font-size:32px;font-weight:400;white-space:nowrap}
.stay p{font-size:12.5px;line-height:22px;margin-top:6px;max-width:190px}
.subscribe{left:680px;top:54px;width:405px;height:46px;display:flex;border-radius:23px;overflow:hidden}
.subscribe span{flex:1;background:#fff;color:#555;font-size:12px;display:flex;align-items:center;padding-left:22px}
.subscribe b{width:92px;background:var(--teal-dark);display:flex;align-items:center;justify-content:center;font-size:16px}
.rule{position:absolute;left:111px;width:977px;height:1px;background:#cfcfcf}
.fnav{left:111px;top:183px;display:flex;gap:38px;font-size:18px;font-weight:700}
.social{left:1003px;top:181px;display:flex;gap:8px}
.social i{display:block;width:22px;height:22px;border-radius:50%;background:#fff}
.social i:first-child{background:var(--teal)}
.contact{top:262px;display:flex;align-items:center;gap:17px;font-size:18px;white-space:nowrap}
.contact .pic{width:26px;height:26px;border-radius:50%;background:#fff;display:flex;align-items:center;justify-content:center}
.contact-btn{left:942px;top:253px;width:130px;height:40px;font-size:15px}
.copy{left:0;width:1200px;top:328px;text-align:center;font-size:13px}
</style>
</head>
<body>

<header class="hero">
  <svg class="hero-wave" width="1200" height="612" viewBox="0 0 1200 612">
    <defs>
      <linearGradient id="heroTeal" x1="0" y1="0" x2="0" y2="1">
        <stop offset="0" stop-color="#3e8185"/>
        <stop offset="1" stop-color="#2a5a5d"/>
      </linearGradient>
    </defs>
    <path d="M0 0 H52 C60 60 40 130 0 160 Z" fill="#2a5a5d"/>
    <path d="M0 380 C60 450 120 500 190 490 C300 470 380 350 520 340 C620 335 680 360 760 380 L1200 420 V612 H0 Z" fill="url(#heroTeal)"/>
  </svg>

  <div class="brand" style="left:110px;top:22px"><span class="brand-dot"></span><span class="brand-name">BriskLoom</span></div>
  <nav class="nav">
    <a class="active">Home</a><a>Product</a><a>Platform</a><a>Company</a><a>News</a>
  </nav>
  <a class="btn btn-teal abs" style="left:957px;top:37px;width:131px;height:39px">Learn More</a>

  <p class="abs hero-kicker">Welcome To</p>
  <h1 class="abs hero-title">Meet <span>BriskLoom</span></h1>
  <a class="btn btn-teal abs" style="left:111px;top:298px;width:131px;height:39px">Get Started</a>

  <div class="abs hero-art" role="img" aria-label="Illustration of a friendly chat robot on a laptop screen with gears and a person working on a laptop"></div>
  <div class="abs dots"><i></i><i></i><i></i></div>
</header>

<section>
  <article class="card" style="left:146px">
    <div class="icon"><svg width="64" height="64" viewBox="0 0 64 64" fill="none" stroke="#2a5a5d" stroke-width="2.5">
      <path d="M32 8 l3 7 7 .5 -5.5 4.5 2 7 -6.5-4 -6.5 4 2-7 -5.5-4.5 7-.5z"/>
      <path d="M6 52 h12 l10 -6 h14 c3 0 3 -4 0 -4 h-12"/>
      <path d="M18 52 v-10 h8 l8 -4"/>
    </svg></div>
    <p>Elevate your users' experience, a new type of conversation awaits.</p>
  </article>
  <article class="card is-active" style="left:459px">
    <div class="icon"><svg width="82" height="82" viewBox="0 0 82 82">
      <circle cx="41" cy="41" r="41" fill="#2a5a5d"/>
      <circle cx="41" cy="38" r="12" fill="none" stroke="#fff" stroke-width="2.5"/>
      <path d="M36 52 h10 M37 57 h8" stroke="#fff" stroke-width="2.5"/>
    </svg></div>
    <p>Enhance your customer experience with BriskLoom's AI Assistant.</p>
  </article>
  <article class="card" style="left:771px">
    <div class="icon"><svg width="64" height="64" viewBox="0 0 64 64" fill="none" stroke="#2a5a5d" stroke-width="3">
      <path d="M10 40 A24 24 0 0 0 56 34"/><path d="M54 24 A24 24 0 0 0 10 30"/>
      <text x="13" y="40" font-family="Lato,sans-serif" font-size="20" font-weight="900" fill="#2a5a5d" stroke="none">24h</text>
    </svg></div>
    <p>Always ready, always on - 24/7</p>
  </article>
</section>

<section class="interactions">
  <h2>Revolutionize your<br><b>customer Interactions</b></h2>
  <p class="lead">All through natural, conversational experiences.</p>

  <div class="benefit" style="top:258px">
    <span class="ic"><svg width="38" height="38" viewBox="0 0 38 38" fill="none" stroke="#2a5a5d" stroke-width="2"><rect x="4" y="5" width="30" height="20" rx="3"/><path d="M10 12h18M10 17h12M16 25v8l5-3"/></svg></span>
    <div><h3>Get answers</h3><p>Users will find the information they need in seconds</p></div>
  </div>
  <div class="benefit" style="top:357px">
    <span class="ic"><svg width="38" height="38" viewBox="0 0 38 38" fill="none" stroke="#2a5a5d" stroke-width="2"><circle cx="19" cy="16" r="9"/><path d="M15 29h8M16 33h6M19 3v3M6 16H3M35 16h-3"/></svg></span>
    <div><h3>Solve Problems</h3><p>Concerns will be addressed quickly with expert assistance</p></div>
  </div>
  <div class="benefit" style="top:456px">
    <span class="ic"><svg width="38" height="38" viewBox="0 0 38 38" fill="none" stroke="#2a5a5d" stroke-width="2"><circle cx="19" cy="12" r="6"/><path d="M4 12h6M28 12h6l-3-3M31 15l3-3M17 20v14M21 24v10"/></svg></span>
    <div><h3>Take Action</h3><p>Users will activate services and features immediately</p></div>
  </div>

  <div class="abs int-art" role="img" aria-label="Illustration of a person at a computer chatting with an AI assistant robot"></div>
</section>

<nav class="tabs">
  <div style="left:115px;top:6px">BriskLoom enables you to</div>
  <div style="left:407px;top:0">Make AI your own with BriskLoom's<br>conversational platform:</div>
  <div class="current" style="left:731px;top:0">BriskLoom prioritizes trust and security:</div>
</nav>

<section class="trust">
  <div class="abs trust-art" role="img" aria-label="Isometric illustration of a cloud-connected laptop, charts and a security shield"></div>
  <h2>Briskloom Prioritizes <b>Trust and Security</b></h2>
  <div class="pillar" style="left:363px">
    <svg width="72" height="66" viewBox="0 0 72 66" fill="none" stroke="#2a5a5d" stroke-width="2.5"><rect x="14" y="4" width="40" height="54" rx="3"/><path d="M22 16h24M22 24h24M22 32h18"/><circle cx="32" cy="52" r="7"/><path d="M29 52l2 2 4-4"/></svg>
    Built-in supervision<br>and auditing
  </div>
  <div class="pillar" style="left:552px;top:136px">
    <svg width="80" height="68" viewBox="0 0 80 68" fill="none" stroke="#2a5a5d" stroke-width="2.5"><circle cx="40" cy="40" r="14"/><circle cx="40" cy="40" r="5"/><path d="M40 26V6M28 30L16 12M52 30l12-18M24 40H6M56 40h18"/></svg>
    Secure integrations
  </div>
  <div class="pillar" style="left:748px;top:136px">
    <svg width="72" height="68" viewBox="0 0 72 68" fill="none" stroke="#2a5a5d" stroke-width="2.5"><ellipse cx="26" cy="12" rx="22" ry="7"/><path d="M4 12v34c0 4 10 7 22 7M48 12v14M4 24c0 4 10 7 22 7M4 36c0 4 10 7 22 7"/><circle cx="50" cy="46" r="13"/><circle cx="50" cy="46" r="5"/></svg>
    Strong data governance<br>and privacy
  </div>
</section>

<div class="footer-bg"></div>

<section class="cta">
  <h2>Discover how BriskLoom can transform your customer<br>experience with customized conversational<br>AI.Contact us today to learn more.</h2>
  <a class="btn btn-white">Learn More</a>
</section>

<footer class="footer">
  <div class="brand" style="left:122px;top:40px"><span class="brand-dot"></span><span class="brand-name">BriskLoom</span></div>
  <div class="abs stay"><h3>Stay Connected</h3><p>Be the first to receive Briskloom update and offerings</p></div>
  <div class="abs subscribe"><span>Enter Email Address</span><b>Sign Up</b></div>

  <div class="rule" style="top:163px"></div>
  <nav class="abs fnav"><a>Home</a><a>Product</a><a>Platform</a><a>Company</a><a>News</a></nav>
  <div class="abs social"><i></i><i></i><i></i></div>
  <div class="rule" style="top:227px"></div>

  <div class="abs contact" style="left:114px">
    <span class="pic"><svg width="14" height="16" viewBox="0 0 14 16"><path d="M7 1a5 5 0 0 1 5 5c0 4-5 9-5 9S2 10 2 6a5 5 0 0 1 5-5z" fill="#2e2f30"/><circle cx="7" cy="6" r="2" fill="#fff"/></svg></span>Lorem ipsum,Usa -437916
  </div>
  <div class="abs contact" style="left:407px">
    <span class="pic"><svg width="14" height="14" viewBox="0 0 14 14"><path d="M3 1l3 3-1.5 1.5c.8 1.7 2.3 3.2 4 4L10 8l3 3-2 2C6 13 1 8 1 3z" fill="#2e2f30"/></svg></span>+1 555 014 2273
  </div>
  <div class="abs contact" style="left:634px">
    <span class="pic"><svg width="14" height="12" viewBox="0 0 14 12"><rect x="1" y="1" width="12" height="10" rx="1" fill="#2e2f30"/><path d="M1.5 2L7 7l5.5-5" stroke="#fff" fill="none"/></svg></span>info@briskloom.example
  </div>
  <a class="btn btn-white abs contact-btn">Contact Us</a>

  <div class="rule" style="top:311px"></div>
  <p class="abs copy">© 2024 BriskLoom . All rights reserved.</p>
</footer>

</body>
</html>
```